Web Design job - Condo Debts Collection Business needs a Web Design

I need a site for a client, who works with condo debts collection, and ensure all revenues provided by condo fees will be always available to the building manager of condo on a specific date, regardless of defaults.
I have the visual identity (logo, slogan and colors) of the company, and some requirements on layout (kind of slider, menu options, phone number on a noble position, etc) - maybe I can do a sketch, but I like the idea of give some freedom to designer.

*** PLEASE, we have no interest in templates. We want something new***

Target Market(s)

I have two targets for this design: - Condominium's building manager. This target is looking for a solution to overdue debts on it's condo. - Residents on condominiums. This target wants to live in a better place, where their neighbors pay their condominium fees on time.

Number of Pages Required

1 page

Requirements
Must have
• - Slider with title, some short text related, a nice image (I prefer happy and/or peaceful family, people doing business, happy friends, and so on).
• - I have a special attention to menu. I'm looking for one I can have a nice effect, more elegant, charming, kind of innovative.
• - Phone number on the top (or clearly visible).
• - Member log in area or icon on the top (or clearly visible).
• - News/articles area.
• - Modern fonts, with good quality, sans-serif on areas where reading is more intensive (prefer Google web-fonts).
• - Colors specified on attached files.
Nice to have
• - Clear background color, cause it's better to read larger texts (like articles). Dark backgrounds makes reading difficult.
• - A site with effects (like shadows, lines, curves, gradients, lights) is usually pretty.
• - I pay attention on beautiful footers.
Should not have
• - Images with a lot of money (I don't sell richness, I sell tranquility, peace, harmony, safety).
• - Poor menu.

```html
<!DOCTYPE html>
<html lang="en">
<head>
<meta charset="utf-8">
<title>Vantora Cobrança Condominial</title>
<link href="https://fonts.googleapis.com/css2?family=Oswald:wght@400;500;600&family=Open+Sans:wght@400;600;700&display=swap" rel="stylesheet">
<style>
:root{
  --gold:#c29b33;
  --gold-dark:#a9852a;
  --yellow:#e3bf2c;
  --about:#dcb934;
  --mission:#b8923a;
  --ink:#1d1d1d;
  --text:#444;
  --muted:#777;
  --panel:#f0f0f0;
  --side:#d9d9d9;
  --footer:#1b1b1b;
  --white:#fff;
}
*{box-sizing:border-box;margin:0;padding:0}
html,body{width:1200px;height:3719px;overflow:hidden}
body{position:relative;background:var(--side);font-family:'Open Sans',sans-serif;color:var(--text)}
.abs{position:absolute}
h1,h2,h3,h4{font-family:'Oswald',sans-serif;font-weight:500;color:var(--ink)}
p{font-size:13px;line-height:25px}

/* header */
.site-header{left:0;top:0;width:1200px;height:170px;background:var(--white)}
.phone-tab{right:10px;top:0;width:300px;height:40px;background:var(--gold);border-radius:0 0 14px 14px;color:#fff;font-size:21px;display:flex;align-items:center;justify-content:center;gap:12px}
.brand{left:82px;top:45px;display:flex;align-items:center;gap:14px}
.brand-mark{width:44px;height:44px;background:var(--yellow)}
.brand-name{font-family:'Oswald',sans-serif;font-weight:600;font-size:52px;color:var(--ink);line-height:1}
.member{left:828px;top:96px;display:flex;align-items:center;gap:10px;font-size:15px;color:#333}
.member .divider{width:1px;height:26px;background:#999;margin:0 10px}
.social-dot{width:16px;height:16px;border-radius:50%;background:#555}

/* hero */
.hero{left:0;top:170px;width:1200px;height:560px;background:linear-gradient(100deg,#6e5b44 0%,#b9946a 28%,#e4cfae 55%,#c9b596 78%,#8c7a62 100%)}
.hero-box{left:87px;top:335px;width:398px;height:230px;background:rgba(189,151,46,.9);padding:26px 30px}
.hero-box h1{color:#fff;font-size:34px;font-weight:400;margin-bottom:14px}
.hero-box p{color:#fff;font-size:14px;line-height:25px}
.btn-outline{display:inline-block;margin-top:20px;border:2px solid #fff;color:#fff;font-size:12px;padding:8px 14px;text-transform:uppercase}
.slide-arrow{width:48px;height:48px;border-radius:50%;border:2px solid #fff;background:rgba(255,255,255,.55)}

/* main column */
.column{left:84px;top:730px;width:1032px;height:2540px;background:var(--white)}
.section-title{position:absolute;left:0;width:1032px;text-align:center;font-size:28px;line-height:36px;text-transform:uppercase}
.lead{position:absolute;left:0;width:1032px;text-align:center;font-size:14px}

.service{top:202px;width:300px;height:393px;background:var(--panel);text-align:center;padding-top:30px}
.service.active{background:var(--gold)}
.service .icon{width:156px;height:156px;border-radius:50%;background:var(--yellow);margin:0 auto;display:flex;align-items:center;justify-content:center}
.service.active .icon{background:#fff}
.service h3{font-family:'Open Sans',sans-serif;font-weight:400;font-size:22px;margin:28px 0 10px}
.service p{padding:0 28px;font-size:14px;line-height:26px}
.service.active h3,.service.active p{color:#fff}

.band{top:651px;width:516px;height:301px;padding:44px 0 0 98px}
.band.about{left:0;background:linear-gradient(90deg,#dcb934,#cfae34)}
.band.mission{left:516px;background:linear-gradient(90deg,#b08a33,#bf9a42);padding-left:86px}
.band h2{color:#fff;font-family:'Open Sans',sans-serif;font-weight:600;font-size:26px}
.band .rule{width:60px;height:3px;background:#fff;margin:8px 0 20px}
.band p{color:#fff;font-size:14px;line-height:26px;width:340px}

.quote{top:1108px;width:290px;height:334px;background:var(--panel)}
.quote .mark{position:absolute;left:-72px;top:-10px;font-family:'Oswald',sans-serif;font-size:78px;color:var(--gold);line-height:1}
.quote .avatar{position:absolute;left:103px;top:-34px;width:84px;height:84px;border-radius:50%;background:linear-gradient(#8a6f5c,#3e342f);border:4px solid #fff}
.quote h4{position:absolute;top:66px;width:100%;text-align:center;font-family:'Open Sans',sans-serif;font-weight:600;font-size:18px}
.quote p{position:absolute;top:104px;padding:0 30px;text-align:center;font-size:14px;line-height:26px}
.quote .role{position:absolute;left:0;bottom:0;width:100%;height:46px;background:var(--gold);color:#fff;font-size:13px;font-style:italic;text-align:center;line-height:46px}
.round-arrow{width:62px;height:62px;border-radius:50%;border:3px solid #111;background:#fff}

.blog-area{left:0;top:1497px;width:1032px;height:593px;background:#f3f3f3}
.post{top:119px;width:320px}
.post .thumb{width:320px;height:224px}
.post h4{font-family:'Open Sans',sans-serif;font-weight:700;font-size:16px;margin:28px 0 8px;color:#222}
.post p{font-size:13px;line-height:23px;color:#333}
.post .meta{margin-top:26px;border-top:1px solid #ccc;border-bottom:1px solid #ccc;height:48px;display:flex;justify-content:space-between;align-items:center;font-size:12px;padding:0 18px}
.post .more{color:var(--gold);font-size:11px;text-transform:uppercase}

.contact-area{left:0;top:2090px;width:1032px;height:394px;background:var(--gold);color:#fff}
.contact-area h2{color:#fff}
.contact-area .lead{color:#fff;font-size:16px;line-height:24px}
.field{background:#fff;color:#666;font-size:13px;padding:0 12px;display:flex;align-items:center}
.field.msg{align-items:flex-start;padding-top:12px}
.submit{background:var(--ink);color:#fff;font-size:13px;display:flex;align-items:center;justify-content:center;text-transform:uppercase}

/* footer */
.site-footer{left:0;top:3269px;width:1200px;height:450px;background:var(--footer);color:#ddd}
.site-footer h4{font-family:'Open Sans',sans-serif;font-weight:700;font-size:15px;color:#fff;text-transform:uppercase}
.contact-line{display:flex;align-items:center;gap:20px;font-size:14px;height:42px}
.link-item{width:210px;height:47px;border-bottom:1px solid #444;font-size:13px;display:flex;align-items:center}
.newsletter-input{width:248px;height:40px;background:#fff;color:#555;font-size:13px;padding:0 10px;display:flex;align-items:center}
.subscribe{width:114px;height:36px;background:var(--gold);color:#fff;font-size:13px;display:flex;align-items:center;justify-content:center}
.foot-social{width:20px;height:20px;border-radius:50%;background:#666}
</style>
</head>
<body>

<header class="site-header abs">
  <div class="phone-tab abs">
    <svg width="20" height="20" viewBox="0 0 24 24"><path fill="#fff" d="M6.6 10.8a15 15 0 0 0 6.6 6.6l2.2-2.2a1 1 0 0 1 1-.25 11.4 11.4 0 0 0 3.6.6 1 1 0 0 1 1 1V20a1 1 0 0 1-1 1A17 17 0 0 1 3 4a1 1 0 0 1 1-1h3.5a1 1 0 0 1 1 1c0 1.25.2 2.45.6 3.6a1 1 0 0 1-.25 1z"/></svg>
    <span>(00) 5555.0142</span>
  </div>
  <div class="brand abs"><span class="brand-mark"></span><span class="brand-name">Vantora</span></div>
  <nav class="member abs">
    <svg width="16" height="14" viewBox="0 0 16 14"><path fill="var(--gold)" d="M0 5h7V1l9 6-9 6V9H0z"/></svg>
    <span>MEMBER LOGIN</span>
    <span class="divider"></span>
    <span class="social-dot"></span><span class="social-dot"></span><span class="social-dot"></span><span class="social-dot"></span>
  </nav>
</header>

<section class="hero abs" role="img" aria-label="Photo of a smiling family with two small children on a sofa in a bright living room">
  <div class="hero-box abs">
    <h1>It's all about quality of life</h1>
    <p>Lorem Ipsum is simply dummy text of the printing and typesetting industry. Lorem Ipsum has been</p>
    <span class="btn-outline">Contact us</span>
  </div>
  <svg class="slide-arrow abs" style="left:12px;top:250px" viewBox="0 0 48 48"><path d="M28 14 18 24l10 10" fill="none" stroke="#333" stroke-width="3"/></svg>
  <svg class="slide-arrow abs" style="left:1134px;top:250px" viewBox="0 0 48 48"><path d="M20 14l10 10-10 10" fill="none" stroke="#333" stroke-width="3"/></svg>
</section>

<main class="column abs">
  <h2 class="section-title" style="top:60px">Welcome to Vantora<br>Cobrança Condominial</h2>
  <p class="lead" style="top:136px">Lorem Ipsum is simply dummy text of the printing and typesetting industry. Lorem Ipsum has been the industry's standard dummy text.</p>

  <article class="service abs" style="left:30px">
    <div class="icon"><svg width="80" height="80" viewBox="0 0 80 80"><path d="M40 10 60 18v16c0 12-9 20-20 24-11-4-20-12-20-24V18z" fill="#fff"/><path d="M31 34l7 7 12-13" fill="none" stroke="var(--yellow)" stroke-width="5"/></svg></div>
    <h3>Liability</h3>
    <p>Lorem Ipsum is simply dummy text of the printing and typesetting industry. Lorem Ipsum has been the industry's standard dummy text ever since the 1500s, when an</p>
  </article>
  <article class="service active abs" style="left:365px">
    <div class="icon"><svg width="80" height="80" viewBox="0 0 80 80"><path d="M34 20H20v40h14" fill="none" stroke="var(--gold)" stroke-width="7"/><path d="M44 22h18M44 40h18M44 58h18" stroke="var(--gold)" stroke-width="7"/><path d="M20 46l-8-6 8-6" fill="var(--gold)"/></svg></div>
    <h3>Lien and Priority</h3>
    <p>Lorem Ipsum is simply dummy text of the printing and typesetting industry. Lorem Ipsum has been the industry's standard dummy text ever since the 1500s, when an</p>
  </article>
  <article class="service abs" style="left:700px">
    <div class="icon"><svg width="80" height="80" viewBox="0 0 80 80"><rect x="34" y="22" width="30" height="38" rx="3" fill="#fff"/><path d="M40 32h18M40 40h18M40 48h12" stroke="var(--yellow)" stroke-width="3"/><circle cx="28" cy="42" r="14" fill="none" stroke="#fff" stroke-width="5"/></svg></div>
    <h3>Revenues Management</h3>
    <p>Lorem Ipsum is simply dummy text of the printing and typesetting industry. Lorem Ipsum has been the industry's standard dummy text ever since the 1500s, when an</p>
  </article>

  <section class="band about abs" role="img" aria-label="Yellow tinted photo of a residential building">
    <h2>About Us</h2><div class="rule"></div>
    <p>Lorem Ipsum is simply dummy text of the printing and typesetting industry. Lorem Ipsum has been the industry's standard dummy text ever since the 1500s, when an unknown printer took a galley of type and scrambled it to make a type specimen</p>
  </section>
  <section class="band mission abs" role="img" aria-label="Gold tinted photo of an office meeting">
    <h2>Our Mission</h2><div class="rule"></div>
    <p>Lorem Ipsum is simply dummy text of the printing and typesetting industry. Lorem Ipsum has been the industry's standard dummy text ever since the 1500s, when an unknown printer took a galley of type and scrambled it to make a type specimen</p>
  </section>

  <h2 class="section-title" style="top:995px">Testimonials</h2>
  <svg class="round-arrow abs" style="left:100px;top:1225px" viewBox="0 0 62 62"><path d="M35 20 24 31l11 11" fill="none" stroke="#111" stroke-width="3"/></svg>
  <svg class="round-arrow abs" style="left:870px;top:1225px" viewBox="0 0 62 62"><path d="M27 20l11 11-11 11" fill="none" stroke="#111" stroke-width="3"/></svg>

  <article class="quote abs" style="left:191px">
    <span class="mark">“</span>
    <div class="avatar" role="img" aria-label="Portrait photo of the client"></div>
    <h4>Marco Feliti</h4>
    <p>Lorem Ipsum is simply dummy text of the printing and typesetting industry. Lorem Ipsum has been the industry's standard dummy text ever since the 1500s, when an unknown printer took a galley of</p>
    <div class="role">Owner, Forno Central</div>
  </article>
  <article class="quote abs" style="left:548px">
    <span class="mark">“</span>
    <div class="avatar" role="img" aria-label="Portrait photo of the client"></div>
    <h4>Lívia Mendes</h4>
    <p>Lorem Ipsum is simply dummy text of the printing and typesetting industry. Lorem Ipsum has been the industry's standard dummy text ever since the 1500s, when an unknown printer took a galley of type and scrambled it to make a</p>
    <div class="role">CEO, Casa Brasa Grill</div>
  </article>

  <section class="blog-area abs">
    <h2 class="section-title" style="top:42px">Recent Blog</h2>
    <article class="post abs" style="left:0">
      <div class="thumb" role="img" aria-label="Photo of a family relaxing on the grass in sunlight" style="background:linear-gradient(160deg,#f3d27a,#a7a04a 55%,#5f7a2c)"></div>
      <h4>HEADING TITLE HERE</h4>
      <p>Lorem Ipsum is simply dummy text of the printing and typesetting industry. Lorem Ipsum has been dummy text ever since the 1500s.</p>
      <div class="meta"><span class="more">Read more ▸</span><span>03/OCT/2017</span></div>
    </article>
    <article class="post abs" style="left:355px">
      <div class="thumb" role="img" aria-label="Photo of business people shaking hands at a desk" style="background:linear-gradient(160deg,#e9eef2,#b9c2c9 50%,#3b3f47)"></div>
      <h4>HEADING TITLE HERE</h4>
      <p>Lorem Ipsum is simply dummy text of the printing and typesetting industry. Lorem Ipsum has been dummy text ever since the 1500s.</p>
      <div class="meta"><span class="more">Read more ▸</span><span>26/SEP/2017</span></div>
    </article>
    <article class="post abs" style="left:712px">
      <div class="thumb" role="img" aria-label="Photo of a modern apartment building under blue sky" style="background:linear-gradient(170deg,#5b9ad8,#a9c6e3 45%,#d8d2c4 70%,#7d9a55)"></div>
      <h4>HEADING TITLE HERE</h4>
      <p>Lorem Ipsum is simply dummy text of the printing and typesetting industry. Lorem Ipsum has been dummy text ever since the 1500s.</p>
      <div class="meta"><span class="more">Read more ▸</span><span>16/SEP/2017</span></div>
    </article>
  </section>

  <section class="contact-area abs">
    <h2 class="section-title" style="top:36px">Send us a message</h2>
    <p class="lead" style="top:90px">Have an Idea for a mobile or web app? Want to market your business in the best way possible?<br>Kindly fill out this form or drop us a line at our mailbox, and we'll be happy to get back to you with solutions and ideas.</p>
    <div class="field msg abs" style="left:30px;top:161px;width:434px;height:176px">Message</div>
    <div class="field abs" style="left:495px;top:161px;width:507px;height:46px">Name</div>
    <div class="field abs" style="left:495px;top:225px;width:507px;height:46px">Email</div>
    <div class="field abs" style="left:495px;top:290px;width:330px;height:46px;justify-content:space-between">Type the code shown<span style="color:#333;font-weight:600">HG845</span></div>
    <div class="submit abs" style="left:846px;top:290px;width:156px;height:46px">Submit</div>
  </section>
</main>

<footer class="site-footer abs">
  <h4 class="abs" style="left:82px;top:62px">Contact us</h4>
  <div class="abs" style="left:82px;top:106px">
    <div class="contact-line"><svg width="16" height="16" viewBox="0 0 24 24"><path fill="#ddd" d="M6.6 10.8a15 15 0 0 0 6.6 6.6l2.2-2.2a1 1 0 0 1 1-.25 11.4 11.4 0 0 0 3.6.6 1 1 0 0 1 1 1V20a1 1 0 0 1-1 1A17 17 0 0 1 3 4a1 1 0 0 1 1-1h3.5a1 1 0 0 1 1 1c0 1.25.2 2.45.6 3.6a1 1 0 0 1-.25 1z"/></svg><span>+123-456-789</span></div>
    <div class="contact-line"><svg width="16" height="18" viewBox="0 0 16 20"><path fill="#ddd" d="M8 0a7 7 0 0 1 7 7c0 5-7 13-7 13S1 12 1 7a7 7 0 0 1 7-7zm0 4a3 3 0 1 0 0 6 3 3 0 0 0 0-6z"/></svg><span>123 Street Name, 46 City Name, Country Name</span></div>
    <div class="contact-line"><svg width="16" height="14" viewBox="0 0 18 14"><rect width="18" height="14" fill="#ddd"/><path d="M0 0l9 7 9-7" fill="none" stroke="#1b1b1b" stroke-width="1.5"/></svg><span>info@domain.com</span></div>
  </div>
  <div class="abs" style="left:82px;top:272px;display:flex;gap:18px">
    <span class="foot-social"></span><span class="foot-social"></span><span class="foot-social"></span><span class="foot-social"></span>
  </div>
  <p class="abs" style="left:82px;top:354px;font-size:12px">© 2018 DOMAIN ALL RIGHTS RESERVED</p>

  <h4 class="abs" style="left:541px;top:62px">Quick links</h4>
  <div class="abs" style="left:541px;top:96px">
    <div class="link-item">LINK NUMBER 1</div><div class="link-item">LINK NUMBER 2</div><div class="link-item">LINK NUMBER 3</div>
    <div class="link-item">LINK NUMBER 4</div><div class="link-item">LINK NUMBER 5</div><div class="link-item">LINK NUMBER 6</div>
  </div>

  <h4 class="abs" style="left:866px;top:62px">Newsletter</h4>
  <p class="abs" style="left:866px;top:100px;width:260px;font-size:13px;line-height:22px">SIGN UP FOR THE LATEST NEWS, OFFERS AND STYLES</p>
  <div class="newsletter-input abs" style="left:866px;top:160px">Your Email</div>
  <div class="subscribe abs" style="left:866px;top:220px">subscribe</div>
  <div class="abs" style="left:866px;top:310px;display:flex;align-items:center;gap:10px">
    <span style="width:30px;height:30px;background:var(--yellow)"></span>
    <span style="font-family:'Oswald',sans-serif;font-weight:600;font-size:38px;color:#fff;line-height:1">Vantora</span>
  </div>
</footer>

</body>
</html>
```